Business Card Design

We are state certified residental contractors who specialize in insurance claims. We are insurance restoration experts and have a state multi-lines insurance adjusters license #W584130. We produce insurance grade estimates using the most widely used software in the industry. Our goal is to work for our customers! not the insurance company. Our edge is we don't take short cuts to please the adjuster/insurance company to insure future claims from them. We are experts at restoring damaged properties.from wind, water ,fire and smoke. We pride ourselfs on evaluating damages properly and providing extremely detailed estimates for restoration.We are also educated and experienced in identifiying and correcting indoor air quality issues as a result of common perils and defective materials. .We are not a franchise and are family owned and operated. We provide quality work using only the best local tradesman. We ourselfs are local tradesmen and helped build and restore our community over the past 30 years. We know first hand how our homes were built and are aware of many of the common problems that exist and how to address them. We are licensed insured and bonded.
Industry/Entity Type
Business
Contact Information for Business Card
Beacon Harbor LLC
Marcus Pelley
4185 Willowbend Rd unit K
Melbourne Fl.32937 Manager/State Certified Residental Contractor license# CRC5871642
321-555-0187 Office
321-555-0162 Fax

```html
<!DOCTYPE html>
<html lang="en">
<head>
<meta charset="utf-8">
<title>Business Card Design</title>
<link rel="stylesheet" href="https://fonts.googleapis.com/css2?family=Alegreya+Sans+SC:wght@700&family=Alegreya:wght@700&family=Arimo:wght@400;700&family=Open+Sans:wght@700&display=swap">
<style>
  :root {
    --stage: #8a8a92;
    --red: #d3212a;
    --blue: #1eb1e6;
    --grey: #8c8c96;
    --white: #ffffff;
  }
  html, body {
    margin: 0;
    padding: 0;
    overflow: hidden;
  }
  .canvas {
    position: relative;
    width: 1200px;
    height: 900px;
    background: var(--stage);
    overflow: hidden;
  }
  .card {
    position: absolute;
    width: 423px;
    height: 248px;
    box-shadow: 0 3px 6px rgba(0, 0, 0, 0.35);
  }
  .card svg { display: block; }
  .card-front { left: 137px; top: 122px; }
  .card-back { left: 649px; top: 542px; }
  .company-name { font-family: "Alegreya Sans SC", sans-serif; font-weight: 700; fill: var(--white); }
  .person-name { font-family: "Alegreya", serif; font-weight: 700; fill: var(--white); font-size: 12px; }
  .body-text { font-family: "Arimo", Arial, sans-serif; fill: var(--white); font-size: 9.5px; }
  .label { font-family: "Open Sans", Arial, sans-serif; font-weight: 700; fill: var(--white); font-size: 10px; }
</style>
</head>
<body>
<main class="canvas">

  <section class="card card-front" aria-label="Business card front">
    <svg width="423" height="248" viewBox="0 0 423 248">
      <defs><clipPath id="front-clip"><rect width="423" height="248"/></clipPath></defs>
      <g clip-path="url(#front-clip)">
        <rect class="band-red" x="0" y="0" width="423" height="63" fill="var(--red)"/>
        <rect class="band-blue" x="0" y="63" width="423" height="120" fill="var(--blue)"/>
        <rect class="band-grey" x="0" y="183" width="423" height="65" fill="var(--grey)"/>
        <circle class="ring-red" cx="316" cy="127" r="77" fill="var(--red)"/>
        <g class="white-edge" fill="var(--white)">
          <rect x="392" y="0" width="31" height="248"/>
          <rect x="357" y="0" width="66" height="41"/>
          <circle cx="357" cy="41" r="43"/>
          <rect x="335" y="204" width="88" height="44"/>
          <circle cx="335" cy="204" r="50"/>
          <circle cx="316" cy="127" r="61"/>
        </g>
        <circle class="logo-dot" cx="316" cy="127" r="42" fill="var(--blue)"/>
        <circle cx="357" cy="41" r="30" fill="var(--red)"/>
        <circle cx="335" cy="204" r="36" fill="var(--grey)"/>
        <g class="icon-globe" fill="none" stroke="var(--white)" stroke-width="1.6">
          <circle cx="335" cy="204" r="12"/>
          <ellipse cx="335" cy="204" rx="5.5" ry="12"/>
          <line x1="323" y1="204" x2="347" y2="204"/>
        </g>
      </g>
      <text class="company-name" x="30" y="118" font-size="25">Company name</text>
      <line x1="30" y1="124" x2="42" y2="124" stroke="var(--white)" stroke-width="1.5"/>
      <line x1="48" y1="124" x2="206" y2="124" stroke="var(--white)" stroke-width="1.5"/>
      <text class="person-name" x="118" y="143" text-anchor="middle">Your Name</text>
      <text class="body-text" x="116" y="154" text-anchor="middle" font-size="9">Your Position</text>
      <text class="body-text" x="73" y="231">www.yourcompany.com</text>
    </svg>
  </section>

  <section class="card card-back" aria-label="Business card back">
    <svg width="423" height="248" viewBox="0 0 423 248">
      <defs><clipPath id="back-clip"><rect width="423" height="248"/></clipPath></defs>
      <g clip-path="url(#back-clip)">
        <rect x="0" y="0" width="423" height="63" fill="var(--red)"/>
        <rect x="0" y="63" width="423" height="120" fill="var(--blue)"/>
        <rect x="0" y="183" width="423" height="65" fill="var(--grey)"/>
        <g class="white-edge" fill="var(--white)">
          <rect x="0" y="0" width="101" height="48"/>
          <rect x="0" y="0" width="82" height="248"/>
          <rect x="0" y="203" width="116" height="45"/>
        </g>
        <circle class="ring-red" cx="141" cy="120" r="77" fill="var(--red)"/>
        <g fill="var(--white)">
          <circle cx="101" cy="48" r="43"/>
          <circle cx="116" cy="203" r="42"/>
          <circle cx="141" cy="120" r="60"/>
        </g>
        <circle cx="141" cy="120" r="44" fill="var(--blue)"/>
        <circle cx="101" cy="48" r="30" fill="var(--red)"/>
        <circle cx="116" cy="203" r="28" fill="var(--grey)"/>
        <path class="icon-phone" d="M92 36 l6 -3 l5 8 l-4 3 q2 6 7 10 l4 -3 l6 6 l-3 5 q-12 0 -21 -26 z" fill="var(--white)"/>
        <path class="icon-house" d="M141 104 l-18 15 h5 v15 h9 v-9 h8 v9 h9 v-15 h5 z" fill="var(--white)"/>
        <g class="icon-envelope">
          <rect x="102" y="194" width="28" height="18" fill="var(--white)"/>
          <polyline points="102,194 116,205 130,194" fill="none" stroke="var(--grey)" stroke-width="1.5"/>
        </g>
      </g>
      <text x="177" y="27"><tspan class="label">PHONE: </tspan><tspan class="body-text" dx="2">+123 456 789</tspan></text>
      <text x="177" y="47"><tspan class="label">MOBILE: </tspan><tspan class="body-text" dx="2">+123 456 789</tspan></text>
      <text x="239" y="121"><tspan class="label">ADDRESS: </tspan><tspan class="body-text">CITY/STATE</tspan></text>
      <text class="body-text" x="239" y="133">ZIP CODE</text>
      <text class="label" x="181" y="215">E-MAIL:</text>
      <text class="body-text" x="181" y="229">abc@yourcompany.com</text>
    </svg>
  </section>

</main>
</body>
</html>
```